Corvane Electronics, Inc. Business card

Incorporate a globe.
We repair electronics, sell electronic parts, and we recycle electronics. We've been in business since 1982. A technology feel to the card is preferred. I want to be able to give this card to a client from different industries and make it relate-able. I don't have a logo that I've been partial to in the past. It is not necessary in this case.

Target Market(s)

Consumer, Industrial, Business, Medical

Industry/Entity Type

Business

Contact Information for Business Card

4518 Maple Crest Blvd. Dallas, TX 75207
214-555-0187 main 214-555-0143 fax
Paul Bredesen VP

Font styles to use
Serif

Requirements
Must have
• Technology feel
Nice to have
• Metallic look
Should not have
• no pastel colors

```html
<!DOCTYPE html>
<html lang="en">
<head>
<meta charset="utf-8">
<title>Corvane Electronics, Inc. — Business Card</title>
<link rel="stylesheet" href="https://fonts.googleapis.com/css2?family=Raleway:wght@500;600&display=swap">
<style>
  :root {
    --stage: #000000;
    --card: #1f252c;
    --card-deep: #1a1f25;
    --accent-blue: #1196e0;
    --mark-white: #ffffff;
    --name-white: #ffffff;
    --name-silver: #bfc2c5;
    --globe-light: #454b52;
    --globe-dark: #2a3037;
  }
  * { margin: 0; padding: 0; box-sizing: border-box; }
  html, body {
    width: 1200px;
    height: 720px;
    overflow: hidden;
    background: var(--stage);
  }
  .card {
    position: absolute;
    left: 38px;
    top: 39px;
    width: 1121px;
    height: 640px;
    overflow: hidden;
    background: radial-gradient(ellipse at 50% 40%, var(--card) 0%, var(--card-deep) 100%);
  }
  .accent-bar {
    position: absolute;
    height: 7px;
    background: var(--accent-blue);
  }
  .accent-bar--top-left { left: 0; top: 29px; width: 57px; }
  .accent-bar--bottom-right { right: 0; top: 603px; width: 61px; }
  .brand {
    position: absolute;
    left: 0;
    right: 0;
    top: 153px;
    display: flex;
    flex-direction: column;
    align-items: center;
    font-family: "Raleway", sans-serif;
    font-weight: 600;
    text-transform: uppercase;
    letter-spacing: -0.5px;
  }
  .brand__mark {
    width: 88px;
    height: 88px;
    border-radius: 50%;
    background: var(--mark-white);
  }
  .brand__name {
    margin-top: 18px;
    font-size: 52px;
    line-height: 62px;
    color: var(--name-white);
  }
  .brand__descriptor {
    margin-top: 0;
    font-size: 52px;
    line-height: 64px;
    color: var(--name-silver);
  }
  .globe {
    position: absolute;
    left: -38px;
    top: 457px;
    width: 266px;
    height: 266px;
    border-radius: 50%;
    background: radial-gradient(circle at 40% 35%, var(--globe-light) 0%, var(--globe-dark) 75%);
    opacity: 0.85;
  }
</style>
</head>
<body>
  <main class="card">
    <div class="accent-bar accent-bar--top-left"></div>
    <div class="accent-bar accent-bar--bottom-right"></div>

    <div class="brand">
      <div class="brand__mark"></div>
      <div class="brand__name">Corvane</div>
      <div class="brand__descriptor">Electronics</div>
    </div>

    <div class="globe" role="img" aria-label="Globe showing the Americas in muted grey tones"></div>
  </main>
</body>
</html>
```